Business Card for a new businees.

need a very good business for a new company based in Riverside California call Levy Lantern LLC. We help client file taxes, resolve tax debt and attain peace of mind We help people nationwide solve Tax problems. We help with Installment agreements, Offers in Compromise, Partial Pay Installment Agreements, Currently Not Collectible status, Liens and Levy Removal, Garnishment removal. We offer individualized services

Target Market(s)

Any one with Tax Problems nationwide. My clients span across age, occupation etc

Contact Information for Business Card

Card must be attractive and have enough information to let client know we care and call us

Colors

Designer to choose colors to be used in the design.

Requirements
Must have
• the basics and then surprise me
Nice to have
• surprise m

```html
<!DOCTYPE html>
<html lang="en">
<head>
<meta charset="utf-8">
<title>Levy Lantern LLC — Business Card</title>
<link href="https://fonts.googleapis.com/css2?family=Poppins:wght@600&family=Work+Sans:wght@400;500;600&display=swap" rel="stylesheet">
<style>
  :root {
    --backdrop: #4a423b;
    --card: #070707;
    --card-sheen: #1c1c1c;
    --gold: #e8c21f;
    --gold-deep: #a8912a;
    --olive: #8f8232;
    --ink-light: #f2f2f2;
  }
  * { margin: 0; padding: 0; box-sizing: border-box; }
  html, body { width: 1200px; height: 930px; overflow: hidden; }
  body {
    background: var(--backdrop);
    font-family: "Work Sans", Arial, sans-serif;
    position: relative;
  }
  .card {
    position: absolute;
    width: 600px;
    height: 343px;
    border-radius: 14px;
    background: linear-gradient(120deg, var(--card) 0%, var(--card-sheen) 45%, var(--card) 60%, var(--card) 100%);
    box-shadow: 0 14px 30px rgba(0,0,0,.45);
    overflow: hidden;
  }
  .card--front { left: 110px; top: 70px; }
  .card--back { left: 490px; top: 500px; }

  .brand { position: absolute; }
  .brand__row { display: flex; align-items: center; gap: 12px; }
  .brand__dot { border-radius: 50%; background: var(--gold); flex: none; }
  .brand__name {
    font-family: "Poppins", Arial, sans-serif;
    font-weight: 600;
    color: var(--gold);
    line-height: 1;
    white-space: nowrap;
  }
  .brand__rule { height: 3px; background: var(--gold); margin: 8px 0 6px; }
  .brand__tagline {
    color: var(--ink-light);
    font-weight: 600;
    letter-spacing: .28em;
    white-space: nowrap;
  }
  .brand__promise {
    color: var(--gold);
    font-weight: 500;
    letter-spacing: .04em;
    white-space: nowrap;
    margin-top: 3px;
  }

  .card--front .brand { left: 110px; top: 125px; }
  .card--front .brand__dot { width: 22px; height: 22px; }
  .card--front .brand__name { font-size: 44px; }
  .card--front .brand__tagline { font-size: 11px; }
  .card--front .brand__promise { font-size: 9px; }

  .card--back .brand { left: 46px; top: 44px; }
  .card--back .brand__dot { width: 13px; height: 13px; }
  .card--back .brand__row { gap: 9px; }
  .card--back .brand__name { font-size: 24px; }
  .card--back .brand__rule { height: 2px; margin: 6px 0 4px; }
  .card--back .brand__tagline { font-size: 6.5px; }
  .card--back .brand__promise { font-size: 5.5px; }

  .person { position: absolute; right: 36px; top: 88px; text-align: right; }
  .person__name {
    font-family: "Poppins", Arial, sans-serif;
    font-weight: 600;
    font-size: 30px;
    color: var(--gold);
    line-height: 1.1;
  }
  .person__role { color: var(--ink-light); font-size: 15px; margin-top: 2px; }

  .divider { position: absolute; left: 40px; right: 36px; top: 156px; height: 1.5px; background: var(--gold); }

  .address {
    position: absolute; right: 36px; top: 170px; text-align: right;
    color: var(--ink-light); font-size: 15px; line-height: 1.4;
  }

  .contacts {
    position: absolute; left: 40px; top: 200px;
    list-style: none; color: var(--ink-light); font-size: 17px;
  }
  .contacts li { display: flex; align-items: center; gap: 12px; line-height: 1.55; }
  .contacts svg { width: 14px; height: 14px; flex: none; }

  .swoosh { position: absolute; left: 0; bottom: 0; width: 600px; height: 120px; }
</style>
</head>
<body>

  <section class="card card--front" aria-label="Card front">
    <div class="brand">
      <div class="brand__row">
        <span class="brand__dot"></span>
        <span class="brand__name">Levy Lantern LLC</span>
      </div>
      <div class="brand__rule"></div>
      <p class="brand__tagline">TAX RELIEF. TAX RETURNS.</p>
      <p class="brand__promise">PEACE OF MIND FOR EVERY TAX PROBLEM, NATIONWIDE</p>
    </div>
  </section>

  <section class="card card--back" aria-label="Card back">
    <div class="brand">
      <div class="brand__row">
        <span class="brand__dot"></span>
        <span class="brand__name">Levy Lantern LLC</span>
      </div>
      <div class="brand__rule"></div>
      <p class="brand__tagline">TAX RELIEF. TAX RETURNS.</p>
      <p class="brand__promise">PEACE OF MIND FOR EVERY TAX PROBLEM, NATIONWIDE</p>
    </div>

    <div class="person">
      <p class="person__name">Dana Whitfield</p>
      <p class="person__role">Director</p>
    </div>

    <div class="divider"></div>

    <p class="address">4250 Orchard Ave. Ste 310<br>Riverside, CA 92501</p>

    <ul class="contacts">
      <li>
        <svg viewBox="0 0 16 16" aria-hidden="true"><path fill="#e8c21f" d="M3.5 1.5l2.5 0 1.2 3-1.6 1.2a8 8 0 0 0 4.7 4.7l1.2-1.6 3 1.2 0 2.5c0 .8-.7 1.5-1.5 1.5A12 12 0 0 1 2 3c0-.8.7-1.5 1.5-1.5z"/></svg>
        951-555-0147
      </li>
      <li>
        <svg viewBox="0 0 16 16" aria-hidden="true"><rect x="1.5" y="3.5" width="13" height="9" fill="none" stroke="#e8c21f" stroke-width="1.5"/><path d="M1.5 3.5l6.5 5 6.5-5" fill="none" stroke="#e8c21f" stroke-width="1.5"/></svg>
        info@levylantern.com
      </li>
      <li>
        <svg viewBox="0 0 16 16" aria-hidden="true"><circle cx="8" cy="8" r="6.3" fill="none" stroke="#e8c21f" stroke-width="1.4"/><path d="M1.7 8h12.6M8 1.7c-3 3.4-3 9.2 0 12.6M8 1.7c3 3.4 3 9.2 0 12.6" fill="none" stroke="#e8c21f" stroke-width="1.2"/></svg>
        www.levylantern.com
      </li>
    </ul>

    <svg class="swoosh" viewBox="0 0 600 120" aria-hidden="true">
      <path d="M0 112 L 410 112 C 450 112 460 62 500 62 L 600 62 L 600 120 L 0 120 Z" fill="var(--olive)"/>
      <path d="M0 98 L 400 98" stroke="var(--gold)" stroke-width="3" fill="none"/>
      <path d="M400 98 C 435 98 450 74 480 74" stroke="var(--gold-deep)" stroke-width="2" fill="none"/>
    </svg>
  </section>

</body>
</html>
```